Professional Facebook Banner, Business Cards, Door Hang Tags, Service Flyer for Pest Control Company

There are really 4 things I need designed but Brief Hive doesn't have them to package together. I am needing to get a Professional Facebook Banner, Business Cards, Door Hang Tags, and Service Flyer for a Pest Control Company. I already have a logo that I will attach to the project along with content a for each one of these tasks. Please see document attached labeled All Design Content & Flyer Content.
Pest Control

```html
<!DOCTYPE html>
<html lang="en">
<head>
<meta charset="utf-8">
<title>Copper Fern Pest Control – Business Cards</title>
<link rel="stylesheet" href="https://fonts.googleapis.com/css2?family=Open+Sans:wght@400;600;700;800&display=swap">
<style>
  :root {
    --orange: #ec6a1f;
    --ink: #0c0c0c;
    --paper: #ffffff;
    --backdrop: #2b2d30;
    --muted: #9a9a9a;
  }
  * { box-sizing: border-box; margin: 0; padding: 0; }
  html, body { width: 1200px; height: 900px; overflow: hidden; }
  body {
    background: var(--backdrop);
    font-family: "Open Sans", Arial, sans-serif;
    position: relative;
  }
  .card {
    position: absolute;
    left: 320px;
    width: 560px;
    height: 320px;
    overflow: hidden;
    box-shadow: 0 10px 30px rgba(0,0,0,.45);
  }

  /* Front */
  .card-front { top: 70px; background: var(--paper); }
  .brand {
    position: absolute; left: 150px; top: 40px;
    display: flex; align-items: center; gap: 14px;
    color: var(--orange); font-weight: 800;
  }
  .brand-mark { width: 22px; height: 22px; background: var(--orange); }
  .brand-name { font-size: 38px; line-height: 1; letter-spacing: 1px; }
  .brand-sub { display: block; font-size: 15px; letter-spacing: 9px; margin-top: 6px; }
  .contact-row {
    position: absolute; left: 40px; top: 150px;
    display: flex; align-items: center; gap: 22px;
  }
  .person { text-align: right; }
  .person-name { color: var(--orange); font-size: 24px; font-weight: 700; line-height: 1.1; }
  .person-role { color: var(--orange); font-size: 13px; font-weight: 400; }
  .divider { width: 2px; height: 46px; background: var(--ink); }
  .contact-lines { color: var(--orange); font-size: 13px; font-weight: 600; line-height: 1.8; }
  .contact-lines svg { width: 12px; height: 12px; vertical-align: -1px; margin-right: 6px; fill: var(--orange); }
  .front-band {
    position: absolute; left: 0; right: 0; bottom: 36px; height: 56px;
    background: var(--ink); color: var(--paper);
    display: flex; align-items: center; padding-left: 40px;
    font-size: 20px; font-weight: 600; letter-spacing: .5px;
  }
  .front-band::after {
    content: ""; position: absolute; left: 0; right: 0; bottom: -36px; height: 14px; background: var(--ink);
  }

  /* Back */
  .card-back { top: 500px; background: var(--ink); color: var(--paper); }
  .services-tab {
    position: absolute; left: 0; top: 26px; height: 46px; width: 380px;
    background: var(--orange);
    clip-path: polygon(0 0, 100% 0, 93% 100%, 0 100%);
    display: flex; align-items: center; padding-left: 36px;
    font-size: 24px; font-weight: 700;
  }
  .tab-slashes { position: absolute; left: 372px; top: 26px; width: 50px; height: 46px; }
  .service-list { position: absolute; list-style: none; font-size: 19px; font-weight: 600; line-height: 1.45; }
  .service-list.col-a { left: 60px; top: 92px; }
  .service-list.col-b { left: 330px; top: 92px; }
  .list-divider { position: absolute; left: 280px; top: 100px; width: 2px; height: 130px; background: var(--muted); transform: rotate(18deg); }
  .back-band {
    position: absolute; left: 0; right: 0; bottom: 22px; height: 44px;
    background: var(--orange);
    display: flex; align-items: center; padding-left: 40px;
    font-size: 21px; font-weight: 700;
  }
</style>
</head>
<body>

<section class="card card-front">
  <div class="brand">
    <span class="brand-mark"></span>
    <div>
      <span class="brand-name">COPPER FERN</span>
      <span class="brand-sub">PEST CONTROL</span>
    </div>
  </div>

  <div class="contact-row">
    <div class="person">
      <p class="person-name">Dale Harmon</p>
      <p class="person-role">Owner</p>
    </div>
    <span class="divider"></span>
    <div class="contact-lines">
      <p><svg viewBox="0 0 24 24"><path d="M6.6 10.8a15 15 0 0 0 6.6 6.6l2.2-2.2a1 1 0 0 1 1-.25 11.4 11.4 0 0 0 3.6.57 1 1 0 0 1 1 1V20a1 1 0 0 1-1 1A17 17 0 0 1 3 4a1 1 0 0 1 1-1h3.5a1 1 0 0 1 1 1c0 1.25.2 2.45.57 3.57a1 1 0 0 1-.25 1z"/></svg>555-014-2290</p>
      <p><svg viewBox="0 0 24 24"><path d="M2 5h20v14H2zm2 2v.5l8 5 8-5V7l-8 5z"/></svg>DALE@COPPERFERNPEST.COM</p>
    </div>
  </div>

  <div class="front-band">www.copperfernpest.com</div>
</section>

<section class="card card-back">
  <div class="services-tab">Services / Inspections</div>
  <svg class="tab-slashes" viewBox="0 0 50 46" aria-hidden="true">
    <polygon points="10,0 18,0 8,46 0,46" fill="#ec6a1f"/>
    <polygon points="24,0 32,0 22,46 14,46" fill="#ec6a1f"/>
    <polygon points="38,0 46,0 36,46 28,46" fill="#ec6a1f"/>
  </svg>

  <ul class="service-list col-a">
    <li>1. Ants</li>
    <li>2. Mosquitos</li>
    <li>3. Fleas</li>
    <li>4. Roaches</li>
    <li>5. Stinging Insects</li>
  </ul>
  <span class="list-divider"></span>
  <ul class="service-list col-b">
    <li>6. Spiders</li>
    <li>7. Rodents</li>
    <li>8. Termites</li>
    <li>9. Mice</li>
    <li>10. Rats</li>
  </ul>

  <div class="back-band">www.copperfernpest.com</div>
</section>

</body>
</html>
```